Home Page Design

Please see design brief attached. Concept here: sketchboard[dot]io/file/qWm83LzpR7cvXuNtYa2KhE/Brindlemoor---Landing-Page?node-id=0%3A1&t=PKr92mvnQsD4xTcZ-1

Industry/Entity Type

Wedding

Number of Pages Required

1 page

Font styles to use
Serif
Sans Serif
Decorative
Script

Colors
A7469A
B969AE
D3A5CF
EDDBEB
F8F0F9
6B429C
8869AF
B7A5CE
E3DAEB
F3F0F8

Requirements
Must have
• Please see attached PDF
Nice to have
• Please see attached PDF
Should not have
• Please see attached PDF

```html
<!DOCTYPE html>
<html lang="en">
<head>
<meta charset="utf-8">
<title>Brindlemoor — Landing Page</title>
<link href="https://fonts.googleapis.com/css2?family=Arimo:wght@400;600;700&family=Damion&display=swap" rel="stylesheet">
<style>
:root{
  --plum:#6B429C;--orchid:#A7469A;--orchid-soft:#B969AE;--mist:#EDDBEB;--blush:#F8F0F9;
  --lilac:#E3DAEB;--haze:#F3F0F8;--ink:#2c2a2e;--muted:#77717a;--night:#1f1e21;
  --band:linear-gradient(90deg,#a1439c 0%,#8a49a6 50%,#6b3fa0 100%);
  --canvas:#f4ecf5;
}
*{box-sizing:border-box;margin:0;padding:0}
html,body{width:1200px;height:2452px;overflow:hidden;background:var(--canvas);font-family:'Arimo',Arial,sans-serif;color:var(--ink)}
.stage{position:relative;width:1261px;height:2576px;transform:scale(.95163);transform-origin:0 0;background:var(--canvas)}
.page{position:absolute;top:81px;width:515px;background:#fff;box-shadow:0 8px 26px rgba(80,40,90,.2);overflow:hidden}
.page--a{left:78px;height:2296px}
.page--b{left:667px;height:2414px}
.sec{position:relative;width:515px;overflow:hidden}
.abs{position:absolute}
.script{font-family:'Damion',cursive;font-weight:400}

/* header */
.topbar{height:46px;background:#fff}
.brand{position:absolute;left:48px;top:16px;font:700 11px 'Arimo',sans-serif;color:var(--plum);letter-spacing:.2px}
.pill{position:absolute;height:20px;border-radius:10px;font:700 6px 'Arimo',sans-serif;letter-spacing:.3px;display:flex;align-items:center;justify-content:center;gap:3px;text-transform:uppercase}
.pill--solid{background:var(--band);color:#fff}
.pill--ghost{background:#fff;color:var(--plum);box-shadow:0 1px 5px rgba(60,30,80,.2)}
.pill--light{background:#fff;color:var(--plum)}
.menu{position:absolute;left:462px;top:21px;width:6px;height:5px;border-top:1px solid #333;border-bottom:1px solid #333}
.menu::after{content:"";position:absolute;left:0;right:0;top:1px;border-top:1px solid #333}
.login{left:333px;top:13px;width:57px}
.signup{left:393px;top:13px;width:57px}

/* hero */
.hero-a{height:436px}
.hero-a__panel{left:0;top:0;width:258px;height:239px;background:#f2e7f3}
.hero-photo{background:linear-gradient(160deg,#3c4a3a 0%,#6b6a4c 35%,#a08566 60%,#d4a86e 80%,#5d4b3b 100%)}
.hero-a__photo{left:258px;top:0;width:257px;height:239px;border-bottom-right-radius:55px}
.hero-title{position:absolute;left:48px;font-size:17px;line-height:21px;color:var(--ink)}
.hero-b .hero-title{color:#fff}
.search-band{left:48px;top:203px;width:420px;height:73px;background:var(--band);border-radius:42px 0 40px 0}
.field{position:absolute;height:21px;border:1px solid rgba(255,255,255,.75);border-radius:11px;color:#fff;font:6px 'Arimo',sans-serif;display:flex;align-items:center;padding-left:9px;gap:4px}
.field--select::after{content:"";position:absolute;right:9px;top:8px;width:3px;height:3px;border-right:1px solid #fff;border-bottom:1px solid #fff;transform:rotate(45deg)}
.search-btn{position:absolute;height:21px;width:53px;border-radius:11px;background:#fff;color:var(--ink);font:700 6px 'Arimo',sans-serif;display:flex;align-items:center;justify-content:center}
.f-loc{left:101px;width:127px}.f-cat{left:231px;width:127px}.f-go{left:361px}

.stat{position:absolute;width:92px;height:85px;background:#fff;border:1px solid #f0e7f1;box-shadow:0 2px 9px rgba(90,50,110,.18);text-align:center}
.stat svg{position:absolute;left:37px;top:14px;width:18px;height:18px}
.stat__num{position:absolute;left:0;right:0;top:37px;font:700 19px 'Arimo',sans-serif;color:var(--plum)}
.stat__label{position:absolute;left:0;right:0;top:64px;font:600 5.5px 'Arimo',sans-serif;letter-spacing:.2px;text-transform:uppercase}
.x1{left:48px}.x2{left:156px}.x3{left:264px}.x4{left:372px}

.hero-b{height:503px}
.hero-b__photo{left:0;top:0;width:515px;height:404px}
.hero-b__wave{left:0;top:0;width:515px;height:404px}
.finder-title{position:absolute;left:0;right:0;top:282px;text-align:center;font-size:20px;color:#fff}

.arrow{position:absolute;width:13px;height:13px;border-radius:50%;display:flex;align-items:center;justify-content:center}
.arrow svg{width:8px;height:8px}
.arrow--ghost{background:#fff;border:1px solid #ddd}
.arrow--fill{background:var(--plum)}
.arrow--white{background:#fff}
.al{left:18px}.ar{left:485px}

/* dark banner */
.promo{height:166px;background:linear-gradient(180deg,#3b3430 0%,#5a4838 40%,#2a2624 100%)}
.center-stack{position:absolute;left:0;right:0;text-align:center;color:#fff}
.promo__title{top:30px;font-size:16px;line-height:20px}
.promo__text{top:87px;font-size:7.3px}
.btn-center{left:229px;width:58px}

/* section titles */
.sec-title{position:absolute;left:0;right:0;text-align:center;font-size:21px;line-height:22px;color:var(--plum)}
.sec-title::after{content:"";display:block;width:22px;height:1.5px;background:var(--orchid);margin:4px auto 0}
.sec-title--light{color:#fff}
.sec-title--light::after{background:#fff}

/* testimonials */
.loves{height:249px;background:#fff}
.quote{position:absolute;top:83px;width:132px;height:92px;background:#fff;box-shadow:0 2px 9px rgba(90,50,110,.16);padding:11px 10px}
.quote h4{font:400 7px 'Arimo',sans-serif;color:var(--ink)}
.stars{color:var(--orchid);font-size:5px;letter-spacing:1px;margin-top:2px}
.quote p{font-size:4.9px;line-height:10.5px;color:var(--muted);margin-top:3px;text-align:justify}
.author{position:absolute;top:183px;display:flex;align-items:center;gap:9px}
.avatar{width:26px;height:26px;border-radius:50%;border:2px solid var(--orchid);background:radial-gradient(circle at 45% 40%,#c49a80,#6d4a3a 70%)}
.author b{display:block;font:700 5.8px 'Arimo',sans-serif;color:var(--orchid)}
.author span{font-size:5.2px;color:var(--muted)}
.c1{left:48px}.c2{left:192px}.c3{left:336px}

/* how it works */
.how{height:245px}
.how__bg{left:0;top:0;width:515px;height:245px;background:linear-gradient(180deg,#fbf3f4 0%,#fff 40%,#fdf5f3 70%,#eedad6 100%)}
.step{position:absolute;top:73px;width:132px;height:144px;background:#fff;box-shadow:0 2px 9px rgba(90,50,110,.16);text-align:center}
.step__icon{position:absolute;left:47px;top:16px;width:37px;height:37px;border-radius:50%;background:var(--band);display:flex;align-items:center;justify-content:center}
.step__icon svg{width:17px;height:17px}
.step h4{position:absolute;left:8px;right:8px;top:64px;font:600 6.6px 'Arimo',sans-serif;line-height:11px;text-transform:uppercase}
.step p{position:absolute;left:7px;right:7px;top:92px;font-size:4.9px;line-height:10.5px;color:var(--muted)}

/* insure band */
.insure{height:176px;background:var(--band)}
.insure__title{top:43px;font-size:16px;line-height:19.5px}
.insure__text{left:72px;right:72px;top:99px;font-size:5.9px;line-height:11.5px}

/* marketplace */
.market{height:315px;background:#fff}
.lede{position:absolute;left:72px;right:72px;text-align:center;font-size:5.9px;line-height:11px;color:var(--muted)}
.tile{position:absolute;width:98px;height:122px;background:#fff;box-shadow:0 2px 9px rgba(90,50,110,.16)}
.tile__img{position:absolute;left:2px;top:2px;right:2px;height:91px}
.tile__label{position:absolute;left:0;right:0;top:104px;text-align:center;font:600 7px 'Arimo',sans-serif;text-transform:uppercase}
.t1{left:48px}.t2{left:156px}.t3{left:263px}.t4{left:370px}
.img-venue{background:linear-gradient(160deg,#f3e6e1,#d8b9b6 55%,#efe5dc)}
.img-photo{background:linear-gradient(160deg,#dfe4e6,#8f8a7a 50%,#b8b59a)}
.img-florist{background:linear-gradient(160deg,#2f2d2f,#d9cbc0 55%,#a9786d)}
.img-cake{background:linear-gradient(160deg,#4e4034,#c7a27c 45%,#e5aab5)}
.img-couple1{background:linear-gradient(160deg,#d2d9de,#6d6f70 55%,#c99ea9)}
.img-couple2{background:linear-gradient(160deg,#eee9e3,#8b8577 50%,#3c3a3b)}
.img-couple3{background:linear-gradient(160deg,#e4eae6,#c9c2b2 50%,#7d8a4a)}
.img-couple4{background:linear-gradient(160deg,#cfd6d4,#8a7c70 50%,#5f6b4a)}
.btn-all{left:212px;top:255px;width:91px;height:19px}

/* pdf */
.pdf{height:243px;background:var(--haze)}
.pdf__ring{left:48px;top:30px;width:184px;height:184px;border-radius:50%;border:3px solid var(--plum);padding:4px;background:#fff}
.pdf__photo{width:100%;height:100%;border-radius:50%;background:radial-gradient(circle at 45% 40%,#c8a38b,#7a5a48 55%,#3b3230)}
.pdf__title{position:absolute;left:258px;top:41px;font-size:15px;line-height:20px;color:var(--plum)}
.pdf__text{position:absolute;left:258px;top:95px;width:210px;font-size:5.8px;line-height:11.5px;color:var(--muted);text-align:justify}
.btn-pdf{left:258px;top:180px;width:82px;height:19px}

/* reclaim */
.reclaim{height:232px;background:var(--band)}
.reclaim--b{height:290px}

/* footer */
.footer{height:188px;background:#ebe0ee}
.footer--b{height:181px;background:var(--night)}
.fcol{position:absolute}
.fcol h5{font:700 6.6px 'Arimo',sans-serif;color:#8a49a6;text-transform:uppercase;margin-bottom:6px;letter-spacing:.2px}
.footer--b .fcol h5{color:#fff}
.fcol li{list-style:none;font-size:5.4px;line-height:14px;color:#3a363c;display:flex;align-items:center;gap:8px}
.footer--b .fcol li{color:#d8d4da}
.fcol li::before{content:"";width:3px;height:3px;border-radius:50%;border:1.2px solid var(--orchid)}
.fcol li.more{color:var(--orchid);font-weight:700}
.k1{left:48px}.k2{left:153px}.k3{left:251px}.k4{left:358px}
.copyright{position:absolute;left:0;right:0;text-align:center;font-size:4.8px;color:#555}
.footer--b .copyright{color:#ccc}
.social{position:absolute;width:14px;height:14px;border-radius:50%;background:#fff;box-shadow:0 1px 4px rgba(0,0,0,.2)}
.social--on{background:var(--plum)}
.s1{left:416px}.s2{left:434px}.s3{left:452px}
</style>
</head>
<body>
<div class="stage">

<!-- ============ Variant A ============ -->
<main class="page page--a">
  <header class="sec topbar">
    <div class="brand">Brindlemoor</div>
    <div class="pill pill--solid login">&#9679; Log in</div>
    <div class="pill pill--ghost signup">&#9679; Sign up</div>
    <div class="menu"></div>
  </header>

  <section class="sec hero-a">
    <div class="abs hero-a__panel"></div>
    <div class="abs hero-a__photo hero-photo" role="img" aria-label="Bride and groom kissing in a meadow at sunset holding sparklers"></div>
    <h1 class="hero-title script" style="top:66px">Be the couple who stuck<br>to their budget!</h1>
    <div class="pill pill--solid" style="left:48px;top:121px;width:57px">Explore</div>
    <div class="abs search-band"></div>
    <div class="field f-loc" style="top:229px">&#9906; Location</div>
    <div class="field field--select f-cat" style="top:229px">Category</div>
    <div class="search-btn f-go" style="top:229px">SEARCH</div>
    <div class="stat x1" style="top:313px"><svg viewBox="0 0 18 18" fill="none" stroke="#6B429C" stroke-width="1.2"><path d="M2 8 9 3l7 5M4 8v8h10V8M7 16v-4h4v4"/></svg><div class="stat__num">700</div><div class="stat__label">Venues</div></div>
    <div class="stat x2" style="top:313px"><svg viewBox="0 0 18 18" fill="none" stroke="#6B429C" stroke-width="1.2"><circle cx="7" cy="11" r="4.5"/><circle cx="11" cy="9" r="4.5"/></svg><div class="stat__num">1500</div><div class="stat__label">Vendors</div></div>
    <div class="stat x3" style="top:313px"><svg viewBox="0 0 18 18" fill="none" stroke="#6B429C" stroke-width="1.2"><path d="M2 4h6l1 1 1-1h6v10h-6l-1 1-1-1H2zM9 5v10"/></svg><div class="stat__num">500</div><div class="stat__label">Weddings booked</div></div>
    <div class="stat x4" style="top:313px"><svg viewBox="0 0 18 18" fill="none" stroke="#6B429C" stroke-width="1.2"><path d="M3 16V8a6 6 0 0 1 12 0v8M6 16V9a3 3 0 0 1 6 0v7"/></svg><div class="stat__num">$7,680</div><div class="stat__label">Averaged saved</div></div>
  </section>

  <section class="sec promo" role="img" aria-label="Wedding guests silhouetted against a sunset ceremony">
    <h2 class="center-stack promo__title script">Because Life is too Short to Wait for<br>Vendors to Reply</h2>
    <p class="center-stack promo__text">Focus on enjoying your wedding! Don't get tied into endless negotiations and emails.</p>
    <div class="pill pill--solid btn-center" style="top:111px">Explore</div>
  </section>

  <section class="sec loves">
    <h2 class="sec-title script" style="top:37px">Our Customer Loves Us</h2>
    <div class="arrow arrow--ghost al" style="top:124px"><svg viewBox="0 0 12 12" fill="none" stroke="#333" stroke-width="1.4"><path d="M7.5 3 4.5 6l3 3"/></svg></div>
    <div class="arrow arrow--fill ar" style="top:124px"><svg viewBox="0 0 12 12" fill="none" stroke="#fff" stroke-width="1.4"><path d="M4.5 3l3 3-3 3"/></svg></div>
    <article class="quote c1"><h4>Lorem ipsum dolor</h4><div class="stars">★★★★★</div><p>Lorem ipsum dolor sit amet, consectetur adipiscing elit, sed do eiusmod tempor inci didunt ut labore et dolore magna aliqua. Ut enim ad minim veniamea.</p></article>
    <article class="quote c2"><h4>Lorem ipsum dolor</h4><div class="stars">★★★★★</div><p>Lorem ipsum dolor sit amet, consectetur adipiscing elit, sed do eiusmod tempor inci didunt ut labore et dolore magna aliqua. Ut enim ad minim veniamea.</p></article>
    <article class="quote c3"><h4>Lorem ipsum dolor</h4><div class="stars">★★★★★</div><p>Lorem ipsum dolor sit amet, consectetur adipiscing elit, sed do eiusmod tempor inci didunt ut labore et dolore magna aliqua. Ut enim ad minim veniamea.</p></article>
    <div class="author c1" style="margin-left:10px"><div class="avatar" role="img" aria-label="Reviewer portrait"></div><div><b>NORA WHITFIELD</b><span>Lorem ipsum dolor sit amet</span></div></div>
    <div class="author c2" style="margin-left:10px"><div class="avatar" role="img" aria-label="Reviewer portrait"></div><div><b>NORA WHITFIELD</b><span>Lorem ipsum dolor sit amet</span></div></div>
    <div class="author c3" style="margin-left:10px"><div class="avatar" role="img" aria-label="Reviewer portrait"></div><div><b>NORA WHITFIELD</b><span>Lorem ipsum dolor sit amet</span></div></div>
  </section>

  <section class="sec how">
    <div class="abs how__bg" role="img" aria-label="Soft watercolour roses and greenery framing the section"></div>
    <h2 class="sec-title script" style="top:28px">How It Works</h2>
    <article class="step c1"><div class="step__icon"><svg viewBox="0 0 18 18" fill="none" stroke="#fff" stroke-width="1.3"><rect x="2" y="3" width="14" height="12" rx="1"/><circle cx="8.5" cy="9.5" r="3"/><path d="M11 12l3 3"/></svg></div><h4>Browse top<br>vendors</h4><p>Lorem ipsum dolor sit amet, consectetur adip iscing elit, sed do eiusmod tempor incifes ut labore et dolore magna aliqua minim veniamea.</p></article>
    <article class="step c2"><div class="step__icon"><svg viewBox="0 0 18 18" fill="none" stroke="#fff" stroke-width="1.3"><rect x="2.5" y="3.5" width="13" height="12" rx="1"/><path d="M2.5 7h13M6 2v3M12 2v3M5 10h2M8 10h2M11 10h2M5 13h2M8 13h2"/></svg></div><h4>Instantly book with<br>pre-negotiated prices</h4><p>Lorem ipsum dolor sit amet, consectetur adip iscing elit, sed do eiusmod tempor incifes ut labore et dolore magna aliqua minim veniamea.</p></article>
    <article class="step c3"><div class="step__icon"><svg viewBox="0 0 18 18" fill="none" stroke="#fff" stroke-width="1.3"><rect x="3" y="2" width="10" height="14" rx="1"/><path d="M5.5 5h5M5.5 8h5"/><circle cx="12.5" cy="12.5" r="3"/></svg></div><h4>Pay over<br>time</h4><p>Lorem ipsum dolor sit amet, consectetur adip iscing elit, sed do eiusmod tempor incifes ut labore et dolore magna aliqua minim veniamea.</p></article>
  </section>

  <section class="sec insure">
    <h2 class="center-stack insure__title script">Brindlewise! - Because life happens. All your<br>bookings are fully insured</h2>
    <p class="center-stack insure__text">Lorem ipsum dolor sit amet, consectetur adipiscing elit, sed do eiusmod tempor incididunt ut labore et dolore magna aliqua. Ut enim ad minim veniam, quis nostrud exercitation ullamco laboris nisi ut aliquip ex ea commodo aute irure dolor in reprehenderit in voluptate velit esse cillum dolorea.</p>
  </section>

  <section class="sec market">
    <h2 class="sec-title script" style="top:40px">Explore Our Marketplace</h2>
    <p class="lede" style="top:77px">Lorem ipsum dolor sit amet, consectetur adipiscing elit, sed do eiusmod tempor incididunt ut labore et dolore magna aliqua ut enim ad minim nostrud exercitation esse cillum dolorea.</p>
    <div class="tile t1" style="top:113px"><div class="tile__img img-venue" role="img" aria-label="Floral wedding reception table"></div><div class="tile__label">Venues</div></div>
    <div class="tile t2" style="top:113px"><div class="tile__img img-photo" role="img" aria-label="Photographer with camera outdoors"></div><div class="tile__label">Photographers</div></div>
    <div class="tile t3" style="top:113px"><div class="tile__img img-florist" role="img" aria-label="Bride holding a bouquet"></div><div class="tile__label">Florists</div></div>
    <div class="tile t4" style="top:113px"><div class="tile__img img-cake" role="img" aria-label="Tiered wedding cake"></div><div class="tile__label">Cakes</div></div>
    <div class="pill pill--solid btn-all">View all categories</div>
  </section>

  <section class="sec pdf">
    <div class="abs pdf__ring"><div class="pdf__photo" role="img" aria-label="Couple embracing, bride wearing a flower crown"></div></div>
    <h2 class="pdf__title script">Download our free PDF and<br>start down the road to saving money</h2>
    <p class="pdf__text">Lorem ipsum dolor sit amet, consectetur adipiscing elit, sed do eiusmod tempor incididunt ut labore et dolore magna aliqua. Ut enim ad minim veniam, quis nostrud exercitation ullamco laboris nisi ut aliquip ex ea commodo conseque irure dolor in reprehende. Dolore magna aliq im ad minim veniam, quis nostrud exercitation ullamco laboris nisi ut aliquip ex ea commodo conseque irure dolorea.</p>
    <div class="pill pill--solid btn-pdf">&#11015; Download PDF</div>
  </section>

  <section class="sec reclaim">
    <h2 class="sec-title sec-title--light script" style="top:30px">Reclaim Your Sanity</h2>
    <div class="arrow arrow--white al" style="top:134px"><svg viewBox="0 0 12 12" fill="none" stroke="#333" stroke-width="1.4"><path d="M7.5 3 4.5 6l3 3"/></svg></div>
    <div class="arrow arrow--white ar" style="top:134px"><svg viewBox="0 0 12 12" fill="none" stroke="#333" stroke-width="1.4"><path d="M4.5 3l3 3-3 3"/></svg></div>
    <div class="tile t1" style="top:80px"><div class="tile__img img-couple1" role="img" aria-label="Newlyweds outside a house"></div><div class="tile__label">Lorum ipsum</div></div>
    <div class="tile t2" style="top:80px"><div class="tile__img img-couple2" role="img" aria-label="Couple cutting the cake"></div><div class="tile__label">Lorum ipsum</div></div>
    <div class="tile t3" style="top:80px"><div class="tile__img img-couple3" role="img" aria-label="Outdoor ceremony chairs and arch"></div><div class="tile__label">Lorum ipsum</div></div>
    <div class="tile t4" style="top:80px"><div class="tile__img img-couple4" role="img" aria-label="Couple hugging in a field"></div><div class="tile__label">Lorum ipsum</div></div>
  </section>

  <footer class="sec footer">
    <div class="fcol k1" style="top:32px"><h5>Local services</h5><ul><li>Wedding Photographers</li><li>Wedding DJs</li><li>Wedding Hair &amp; Makeup</li><li>Wedding Planners</li><li>Wedding Caterers</li><li>Wedding Florists</li><li>Wedding Videographers</li><li class="more">MORE</li></ul></div>
    <div class="fcol k2" style="top:32px"><h5>Digital services</h5><ul><li>Logo Design</li><li>Portraits &amp; Caricatures</li><li>Video Editing</li><li>Invitation Design</li><li>Image Editing</li><li>Slideshow Videos</li><li>Speechwriting</li><li>Greeting Cards &amp; Videos</li></ul></div>
    <div class="fcol k3" style="top:32px"><h5>Support</h5><ul><li>Help &amp; Support</li><li>Trust &amp; Safety</li><li>Selling on Brindlemoor</li><li>Buying on Brindlemoor</li></ul></div>
    <div class="fcol k4" style="top:32px"><h5>More from Brindlemoor</h5><ul><li>Brindlemoor Business</li><li>Brindlemoor Pro</li><li>Careers</li><li>Press &amp; News</li><li>Partnership</li><li>Privacy Policy</li><li>Terms of Service</li></ul></div>
    <p class="copyright" style="top:170px">© 2022 BRINDLEMOOR &nbsp;|&nbsp; All Rights Reserved</p>
    <div class="social social--on s1" style="top:166px"></div>
    <div class="social s2" style="top:166px"></div>
    <div class="social s3" style="top:166px"></div>
  </footer>
</main>

<!-- ============ Variant B ============ -->
<main class="page page--b">
  <header class="sec topbar">
    <div class="brand">Brindlemoor</div>
    <div class="pill pill--solid login">&#9679; Log in</div>
    <div class="pill pill--ghost signup">&#9679; Sign up</div>
    <div class="menu"></div>
  </header>

  <section class="sec hero-b">
    <div class="abs hero-b__photo hero-photo" role="img" aria-label="Bride and groom kissing in a meadow at sunset holding sparklers"></div>
    <svg class="abs hero-b__wave" viewBox="0 0 515 404" preserveAspectRatio="none">
      <defs><linearGradient id="bandB" x1="0" x2="1"><stop offset="0" stop-color="#a1439c"/><stop offset=".5" stop-color="#8a49a6"/><stop offset="1" stop-color="#6b3fa0"/></linearGradient></defs>
      <path d="M0 250C90 202 180 200 300 214S470 200 515 160V404H0Z" fill="url(#bandB)"/>
      <path d="M0 241C90 193 180 191 300 205S470 191 515 151" fill="none" stroke="#fff" stroke-width="3"/>
    </svg>
    <h1 class="hero-title script" style="top:70px">Be the couple who stuck<br>to their budget!</h1>
    <div class="pill pill--solid" style="left:48px;top:125px;width:57px">Explore</div>
    <div class="arrow arrow--white al" style="top:110px"><svg viewBox="0 0 12 12" fill="none" stroke="#333" stroke-width="1.4"><path d="M7.5 3 4.5 6l3 3"/></svg></div>
    <div class="arrow arrow--white ar" style="top:110px"><svg viewBox="0 0 12 12" fill="none" stroke="#333" stroke-width="1.4"><path d="M4.5 3l3 3-3 3"/></svg></div>
    <h2 class="finder-title script">Find Vendors</h2>
    <div class="field f-loc" style="top:325px">&#9906; Location</div>
    <div class="field field--select f-cat" style="top:325px">Category</div>
    <div class="search-btn f-go" style="top:325px">SEARCH</div>
    <div class="stat x1" style="top:372px"><svg viewBox="0 0 18 18" fill="none" stroke="#6B429C" stroke-width="1.2"><path d="M2 8 9 3l7 5M4 8v8h10V8M7 16v-4h4v4"/></svg><div class="stat__num">700</div><div class="stat__label">Venues</div></div>
    <div class="stat x2" style="top:372px"><svg viewBox="0 0 18 18" fill="none" stroke="#6B429C" stroke-width="1.2"><circle cx="7" cy="11" r="4.5"/><circle cx="11" cy="9" r="4.5"/></svg><div class="stat__num">1500</div><div class="stat__label">Vendors</div></div>
    <div class="stat x3" style="top:372px"><svg viewBox="0 0 18 18" fill="none" stroke="#6B429C" stroke-width="1.2"><path d="M2 4h6l1 1 1-1h6v10h-6l-1 1-1-1H2zM9 5v10"/></svg><div class="stat__num">500</div><div class="stat__label">Weddings booked</div></div>
    <div class="stat x4" style="top:372px"><svg viewBox="0 0 18 18" fill="none" stroke="#6B429C" stroke-width="1.2"><path d="M3 16V8a6 6 0 0 1 12 0v8M6 16V9a3 3 0 0 1 6 0v7"/></svg><div class="stat__num">$7,680</div><div class="stat__label">Averaged saved</div></div>
  </section>

  <section class="sec promo" role="img" aria-label="Wedding guests silhouetted against a sunset ceremony">
    <h2 class="center-stack promo__title script">Because Life is too Short to Wait for<br>Vendors to Reply</h2>
    <p class="center-stack promo__text">Focus on enjoying your wedding! Don't get tied into endless negotiations and emails.</p>
    <div class="pill pill--solid btn-center" style="top:111px">Explore</div>
  </section>

  <section class="sec loves">
    <h2 class="sec-title script" style="top:37px">Our Customer Loves Us</h2>
    <div class="arrow arrow--ghost al" style="top:124px"><svg viewBox="0 0 12 12" fill="none" stroke="#333" stroke-width="1.4"><path d="M7.5 3 4.5 6l3 3"/></svg></div>
    <div class="arrow arrow--fill ar" style="top:124px"><svg viewBox="0 0 12 12" fill="none" stroke="#fff" stroke-width="1.4"><path d="M4.5 3l3 3-3 3"/></svg></div>
    <article class="quote c1"><h4>Lorem ipsum dolor</h4><div class="stars">★★★★★</div><p>Lorem ipsum dolor sit amet, consectetur adipiscing elit, sed do eiusmod tempor inci didunt ut labore et dolore magna aliqua. Ut enim ad minim veniamea.</p></article>
    <article class="quote c2"><h4>Lorem ipsum dolor</h4><div class="stars">★★★★★</div><p>Lorem ipsum dolor sit amet, consectetur adipiscing elit, sed do eiusmod tempor inci didunt ut labore et dolore magna aliqua. Ut enim ad minim veniamea.</p></article>
    <article class="quote c3"><h4>Lorem ipsum dolor</h4><div class="stars">★★★★★</div><p>Lorem ipsum dolor sit amet, consectetur adipiscing elit, sed do eiusmod tempor inci didunt ut labore et dolore magna aliqua. Ut enim ad minim veniamea.</p></article>
    <div class="author c1" style="margin-left:10px"><div class="avatar" role="img" aria-label="Reviewer portrait"></div><div><b>NORA WHITFIELD</b><span>Lorem ipsum dolor sit amet</span></div></div>
    <div class="author c2" style="margin-left:10px"><div class="avatar" role="img" aria-label="Reviewer portrait"></div><div><b>NORA WHITFIELD</b><span>Lorem ipsum dolor sit amet</span></div></div>
    <div class="author c3" style="margin-left:10px"><div class="avatar" role="img" aria-label="Reviewer portrait"></div><div><b>NORA WHITFIELD</b><span>Lorem ipsum dolor sit amet</span></div></div>
  </section>

  <section class="sec how">
    <div class="abs how__bg" role="img" aria-label="Soft watercolour roses and greenery framing the section"></div>
    <h2 class="sec-title script" style="top:28px">How It Works</h2>
    <article class="step c1"><div class="step__icon"><svg viewBox="0 0 18 18" fill="none" stroke="#fff" stroke-width="1.3"><rect x="2" y="3" width="14" height="12" rx="1"/><circle cx="8.5" cy="9.5" r="3"/><path d="M11 12l3 3"/></svg></div><h4>Browse top<br>vendors</h4><p>Lorem ipsum dolor sit amet, consectetur adip iscing elit, sed do eiusmod tempor incifes ut labore et dolore magna aliqua minim veniamea.</p></article>
    <article class="step c2"><div class="step__icon"><svg viewBox="0 0 18 18" fill="none" stroke="#fff" stroke-width="1.3"><rect x="2.5" y="3.5" width="13" height="12" rx="1"/><path d="M2.5 7h13M6 2v3M12 2v3M5 10h2M8 10h2M11 10h2M5 13h2M8 13h2"/></svg></div><h4>Instantly book with<br>pre-negotiated prices</h4><p>Lorem ipsum dolor sit amet, consectetur adip iscing elit, sed do eiusmod tempor incifes ut labore et dolore magna aliqua minim veniamea.</p></article>
    <article class="step c3"><div class="step__icon"><svg viewBox="0 0 18 18" fill="none" stroke="#fff" stroke-width="1.3"><rect x="3" y="2" width="10" height="14" rx="1"/><path d="M5.5 5h5M5.5 8h5"/><circle cx="12.5" cy="12.5" r="3"/></svg></div><h4>Pay over<br>time</h4><p>Lorem ipsum dolor sit amet, consectetur adip iscing elit, sed do eiusmod tempor incifes ut labore et dolore magna aliqua minim veniamea.</p></article>
  </section>

  <section class="sec insure">
    <h2 class="center-stack insure__title script">Brindlewise! - Because life happens. All your<br>bookings are fully insured</h2>
    <p class="center-stack insure__text">Lorem ipsum dolor sit amet, consectetur adipiscing elit, sed do eiusmod tempor incididunt ut labore et dolore magna aliqua. Ut enim ad minim veniam, quis nostrud exercitation ullamco laboris nisi ut aliquip ex ea commodo aute irure dolor in reprehenderit in voluptate velit esse cillum dolorea.</p>
  </section>

  <section class="sec market">
    <h2 class="sec-title script" style="top:40px">Explore Our Marketplace</h2>
    <p class="lede" style="top:77px">Lorem ipsum dolor sit amet, consectetur adipiscing elit, sed do eiusmod tempor incididunt ut labore et dolore magna aliqua ut enim ad minim nostrud exercitation esse cillum dolorea.</p>
    <div class="tile t1" style="top:113px"><div class="tile__img img-venue" role="img" aria-label="Floral wedding reception table"></div><div class="tile__label">Venues</div></div>
    <div class="tile t2" style="top:113px"><div class="tile__img img-photo" role="img" aria-label="Photographer with camera outdoors"></div><div class="tile__label">Photographers</div></div>
    <div class="tile t3" style="top:113px"><div class="tile__img img-florist" role="img" aria-label="Bride holding a bouquet"></div><div class="tile__label">Florists</div></div>
    <div class="tile t4" style="top:113px"><div class="tile__img img-cake" role="img" aria-label="Tiered wedding cake"></div><div class="tile__label">Cakes</div></div>
    <div class="pill pill--solid btn-all">View all categories</div>
  </section>

  <section class="sec pdf">
    <div class="abs pdf__ring"><div class="pdf__photo" role="img" aria-label="Couple embracing, bride wearing a flower crown"></div></div>
    <h2 class="pdf__title script">Download our free PDF and<br>start down the road to saving money</h2>
    <p class="pdf__text">Lorem ipsum dolor sit amet, consectetur adipiscing elit, sed do eiusmod tempor incididunt ut labore et dolore magna aliqua. Ut enim ad minim veniam, quis nostrud exercitation ullamco laboris nisi ut aliquip ex ea commodo conseque irure dolor in reprehende. Dolore magna aliq im ad minim veniam, quis nostrud exercitation ullamco laboris nisi ut aliquip ex ea commodo conseque irure dolorea.</p>
    <div class="pill pill--solid btn-pdf">&#11015; Download PDF</div>
  </section>

  <section class="sec reclaim reclaim--b">
    <h2 class="sec-title sec-title--light script" style="top:30px">Reclaim Your Sanity</h2>
    <div class="arrow arrow--white al" style="top:134px"><svg viewBox="0 0 12 12" fill="none" stroke="#333" stroke-width="1.4"><path d="M7.5 3 4.5 6l3 3"/></svg></div>
    <div class="arrow arrow--white ar" style="top:134px"><svg viewBox="0 0 12 12" fill="none" stroke="#333" stroke-width="1.4"><path d="M4.5 3l3 3-3 3"/></svg></div>
    <div class="tile t1" style="top:80px"><div class="tile__img img-couple1" role="img" aria-label="Newlyweds outside a house"></div><div class="tile__label">Lorum ipsum</div></div>
    <div class="tile t2" style="top:80px"><div class="tile__img img-couple2" role="img" aria-label="Couple cutting the cake"></div><div class="tile__label">Lorum ipsum</div></div>
    <div class="tile t3" style="top:80px"><div class="tile__img img-couple3" role="img" aria-label="Outdoor ceremony chairs and arch"></div><div class="tile__label">Lorum ipsum</div></div>
    <div class="tile t4" style="top:80px"><div class="tile__img img-couple4" role="img" aria-label="Couple hugging in a field"></div><div class="tile__label">Lorum ipsum</div></div>
    <svg class="abs" style="left:0;bottom:0" width="515" height="80" viewBox="0 0 515 80" preserveAspectRatio="none">
      <path d="M0 80V62C110 20 290 66 420 36C470 24 500 12 515 0V80Z" fill="#1f1e21"/>
      <path d="M0 56C110 14 290 60 420 30C470 18 500 6 515-6" fill="none" stroke="#fff" stroke-width="4"/>
    </svg>
  </section>

  <footer class="sec footer footer--b">
    <div class="fcol k1" style="top:20px"><h5>Local services</h5><ul><li>Wedding Photographers</li><li>Wedding DJs</li><li>Wedding Hair &amp; Makeup</li><li>Wedding Planners</li><li>Wedding Caterers</li><li>Wedding Florists</li><li>Wedding Videographers</li><li class="more">MORE</li></ul></div>
    <div class="fcol k2" style="top:20px"><h5>Digital services</h5><ul><li>Logo Design</li><li>Portraits &amp; Caricatures</li><li>Video Editing</li><li>Invitation Design</li><li>Image Editing</li><li>Slideshow Videos</li><li>Speechwriting</li><li>Greeting Cards &amp; Videos</li></ul></div>
    <div class="fcol k3" style="top:20px"><h5>Support</h5><ul><li>Help &amp; Support</li><li>Trust &amp; Safety</li><li>Selling on Brindlemoor</li><li>Buying on Brindlemoor</li></ul></div>
    <div class="fcol k4" style="top:20px"><h5>More from Brindlemoor</h5><ul><li>Brindlemoor Business</li><li>Brindlemoor Pro</li><li>Careers</li><li>Press &amp; News</li><li>Partnership</li><li>Privacy Policy</li><li>Terms of Service</li></ul></div>
    <p class="copyright" style="top:162px">© 2022 BRINDLEMOOR &nbsp;|&nbsp; All Rights Reserved</p>
    <div class="social social--on s1" style="top:158px"></div>
    <div class="social s2" style="top:158px"></div>
    <div class="social s3" style="top:158px"></div>
  </footer>
</main>

</div>
</body>
</html>
```